International Supplier needs an eye catching profssional letterhead and continuation page

We need a letterhead and continuation sheet designed for a company based in Austria called VELMA Screens GmbH. We develop and install innovate glass partition wall solutions to commercial and cultural buildings and to some of the most contemporary architectural buildings in Europe. I have our inhouse design brief confirming our corporate colours, fonts and images and have our corporate logo available in a variety of formats including AI and EPS. We are open to differing design suggestions as long as they follow the colour and font specification in our corporate design brief. We are at the forefront of innovation, craftmanship and design for architectural glass, framing systems and fire rated partition systems. The final design should communicate the spirit and strength of the company.
www.velma.com / www.tarnovu.co.uk / www.brandpane.com

Target Market(s)

Architects, planners, designers, building contractors and construction companies

Industry/Entity Type

Architecture

Font styles to use
Sans Serif

Requirements
Must have
• VELMA Screens GmbH
• Lindorfergasse 4 B
• 7000 Eisenstadt
• Österreich
• Tel: +43 (1) 482 6170
• E-mail:office@velmascreens.at
• Web:www.velmascreens.at / www.velmabrandpane.com
• subtle yet professionally distinctive
• colours and fonts to be taken ffom VELMA design guide but we are also open to variations on the same theme
Should not have
• No bold lines

```html
<!DOCTYPE html>
<html lang="en">
<head>
<meta charset="utf-8">
<title>VELMA Screens GmbH – Letterhead</title>
<link href="https://fonts.googleapis.com/css2?family=Lato:wght@400;700&family=Tinos:wght@400;700&display=swap" rel="stylesheet">
<style>
  :root {
    --backdrop: #6b6b6b;
    --paper: #fafafa;
    --ink: #1c1c1c;
    --brand-red: #c8102e;
    --rule: #7a7a7a;
  }
  * { margin: 0; padding: 0; box-sizing: border-box; }
  html, body {
    width: 1200px; height: 1200px; overflow: hidden;
    background: var(--backdrop);
  }
  .sheet {
    position: absolute; left: 220px; top: 31px;
    width: 760px; height: 1138px;
    background: var(--paper);
    color: var(--ink);
  }
  .brand {
    position: absolute; left: 56px; top: 72px;
    display: flex; align-items: center; gap: 14px;
  }
  .brand-mark { width: 60px; height: 60px; background: var(--brand-red); }
  .brand-name {
    font-family: "Lato", sans-serif; font-weight: 400;
    font-size: 86px; line-height: 1; letter-spacing: 1px; color: var(--ink);
  }
  .contact {
    position: absolute; right: 57px; top: 95px;
    font-family: "Lato", sans-serif; font-size: 14px; line-height: 18px;
    text-align: right; list-style: none;
  }
  .contact li { display: flex; justify-content: flex-end; align-items: center; gap: 5px; }
  .contact svg { width: 10px; height: 10px; fill: var(--brand-red); }
  .letter {
    position: absolute; left: 69px; right: 69px;
    font-family: "Tinos", serif; font-size: 15px; line-height: 18.5px;
  }
  .letter p { text-align: justify; }
  .issue-date { top: 228px; }
  .recipient { top: 300px; }
  .subject { top: 411px; font-weight: 700; }
  .salutation { top: 484px; }
  .body { top: 521px; }
  .body p + p { margin-top: 18px; }
  .closing { top: 743px; }
  .footer-url {
    position: absolute; left: 0; right: 0; top: 1035px; text-align: center;
    font-family: "Lato", sans-serif; font-size: 17px; letter-spacing: 2.6px;
    color: var(--brand-red);
  }
  .footer-rule {
    position: absolute; left: 49px; width: 662px; top: 1067px;
    border-top: 1px solid var(--rule);
  }
  .footer-address {
    position: absolute; left: 0; right: 0; top: 1078px; text-align: center;
    font-family: "Lato", sans-serif; font-size: 16px; word-spacing: 1px;
  }
</style>
</head>
<body>
<main class="sheet">
  <header>
    <div class="brand">
      <span class="brand-mark" aria-hidden="true"></span>
      <span class="brand-name">VELMA</span>
    </div>
    <ul class="contact">
      <li>+43 (1) 482 6170
        <svg viewBox="0 0 10 10" aria-hidden="true"><path d="M1 4 Q5 0 9 4 L8 5 L6.5 4 L6.5 3 Q5 2.5 3.5 3 L3.5 4 L2 5 Z M2.5 5.5 H7.5 L8.5 9 H1.5 Z"/></svg></li>
      <li>office@velmascreens.at
        <svg viewBox="0 0 10 10" aria-hidden="true"><path d="M1 2 H9 V8 H1 Z M1.5 2.5 L5 5.5 L8.5 2.5" /></svg></li>
      <li>www.velmascreens.at
        <svg viewBox="0 0 10 10" aria-hidden="true"><circle cx="5" cy="5" r="4.5"/></svg></li>
    </ul>
  </header>

  <p class="letter issue-date">Issuing date: May 5, 2012</p>
  <address class="letter recipient" style="font-style:normal">
    Name of employee: Mr. xyz<br>Address of employee<br>address line 2
  </address>
  <p class="letter subject">Ref: Promotion as an Assistant secretary</p>
  <p class="letter salutation">Dear Mr. xyz,</p>
  <section class="letter body">
    <p>I have the pleasure to inform you that you have been promoted as assistant secretary in the share department of the company. You are required to take charge of the new assignment on 15<sup style="font-size:9px">th</sup> May, 2012. Please accept my hearty congratulations on your promotion.</p>
    <p>Your salary scale in the promoted cadre will be Tk. 16,000 and from 15th may, your basic salary will be fixed at Tk. 12,000 in the said scale. You will be entitled to all other allowances as applicable to the staff-II of the company. Other services conditions remain unchanged.</p>
    <p>Please acknowledge receipt of this letter.</p>
  </section>
  <p class="letter closing">Yours sincerely,</p>

  <footer>
    <p class="footer-url">www.velmabrandpane.com</p>
    <div class="footer-rule"></div>
    <p class="footer-address">Lindorfergasse 4 B&nbsp; 7000 Eisenstadt&nbsp; Österreich</p>
  </footer>
</main>
</body>
</html>
```